Geschäftspapiere für Unternehmensberatung
Zielgruppe
Wir machen Unternehmensberatung, Prozessoptimierung, Change Management,
Buchhaltung.
Unsere Zielgruppe sind Firmen, denen es wirtschaftlich nicht so gut geht und die Hilfe benötigen.
Aufgabenstellung
Wir möchten ein CI an unser Logo angepasst.
Es darf gerne etwas besonderes sein.

```html
<!DOCTYPE html>
<html lang="de">
<head>
<meta charset="utf-8">
<title>Meridan Consulting – Geschäftspapiere</title>
<link rel="stylesheet" href="https://fonts.googleapis.com/css2?family=Open+Sans:wght@400;600&display=swap">
<style>
  :root {
    --bg: #e4e4e7;
    --paper: #f4f5f7;
    --dark: #2a2a2c;
    --dark-deep: #1e1e20;
    --brand-grey: #a3a4a8;
    --brand-grey-dark: #6f7074;
    --text-dark: #3a3a3c;
    --text-light: #d6d6d8;
  }
  * { box-sizing: border-box; margin: 0; padding: 0; }
  html, body { width: 1200px; height: 805px; overflow: hidden; }
  body {
    background: var(--bg);
    position: relative;
    font-family: "Open Sans", Arial, sans-serif;
  }
  .sheet { position: absolute; box-shadow: 0 8px 18px rgba(0,0,0,.18); overflow: hidden; }

  .brand { display: flex; align-items: center; gap: 5px; font-family: "Open Sans", Arial, sans-serif; font-weight: 600; color: var(--brand-grey); white-space: nowrap; letter-spacing: .02em; }
  .brand-mark { background: var(--brand-grey); flex: none; }
  .brand-sm { font-size: 8px; } .brand-sm .brand-mark { width: 7px; height: 7px; }
  .brand-md { font-size: 10px; } .brand-md .brand-mark { width: 8px; height: 8px; }
  .brand-lg { font-size: 11.5px; } .brand-lg .brand-mark { width: 9px; height: 9px; }
  .brand.on-light { color: var(--brand-grey-dark); }
  .brand.on-light .brand-mark { background: var(--brand-grey-dark); }

  /* Business cards */
  .card { width: 140px; height: 84px; background: var(--dark); border-radius: 6px; top: 128px; }
  .card-front { left: 36px; display: flex; align-items: center; justify-content: center; }
  .card-back { left: 190px; padding: 12px 12px; color: var(--text-light); font-size: 5.5px; line-height: 1.6; }
  .card-back .person { font-size: 7px; font-weight: 600; color: var(--brand-grey); }
  .card-back .role { color: var(--brand-grey); margin-bottom: 5px; }

  /* Letterhead */
  .letterhead { left: 378px; top: 104px; width: 302px; height: 428px; background: var(--paper); }
  .letterhead .tab { position: absolute; left: 98px; top: 0; width: 89px; height: 11px; background: var(--dark-deep); }
  .letterhead .head { position: absolute; top: 25px; left: 0; right: 0; display: flex; justify-content: center; }
  .letterhead .foot { position: absolute; top: 365px; left: 0; right: 0; display: flex; flex-direction: column; align-items: center; gap: 7px; }
  .letterhead .legal { font-size: 5px; line-height: 1.55; color: var(--text-dark); text-align: center; }
  .letterhead .base { position: absolute; left: 0; right: 0; bottom: 0; height: 5px; background: var(--dark); }

  /* Envelope */
  .envelope { left: 344px; top: 562px; width: 336px; height: 170px; background: var(--paper); }
  .envelope .flap { position: absolute; left: 0; top: 0; width: 336px; height: 45px; background: var(--dark); border-radius: 0 0 14px 14px; display: flex; align-items: center; justify-content: center; }

  /* Compliment card */
  .compliment { left: 733px; top: 72px; width: 341px; height: 172px; background: linear-gradient(160deg, var(--dark-deep), var(--dark)); }
  .compliment .brand { position: absolute; left: 30px; top: 36px; }
  .compliment .contact { position: absolute; right: 20px; top: 108px; text-align: right; color: var(--text-light); font-size: 4.6px; line-height: 1.6; }
  .compliment .rule { height: 1px; background: var(--text-light); opacity: .6; margin: 3px 0 3px 30px; }

  /* Folder */
  .folder { left: 732px; top: 260px; width: 341px; height: 449px; background: linear-gradient(90deg, var(--dark-deep), var(--dark)); }
  .folder .brand { position: absolute; left: 31px; top: 393px; }
</style>
</head>
<body>

  <section class="sheet card card-front" aria-label="Visitenkarte Vorderseite">
    <div class="brand brand-sm"><span class="brand-mark"></span>Meridan Consulting</div>
  </section>

  <section class="sheet card card-back" aria-label="Visitenkarte Rückseite">
    <p class="person">Owen Harlow</p>
    <p class="role">Director</p>
    <p>T: (403) 555-0187</p>
    <p>info@meridanconsult.com</p>
    <p>www.meridanconsult.com</p>
    <p>42 - 8 Ave SW, Calgary</p>
  </section>

  <section class="sheet letterhead" aria-label="Briefbogen">
    <div class="tab"></div>
    <div class="head"><div class="brand brand-md on-light"><span class="brand-mark"></span>Meridan Consulting</div></div>
    <div class="foot">
      <div class="brand brand-sm on-light"><span class="brand-mark"></span>Meridan Consulting</div>
      <p class="legal">RC: 2741 - patente: 38216094 - I.F : 51093386<br>CNSS: 6018270 - ICE: 002715630000047<br>Siège social : N7, Rue des Lilas 20250 Oudaya</p>
    </div>
    <div class="base"></div>
  </section>

  <section class="sheet envelope" aria-label="Briefumschlag">
    <div class="flap"><div class="brand brand-md"><span class="brand-mark"></span>Meridan Consulting</div></div>
  </section>

  <section class="sheet compliment" aria-label="Kurzmitteilung">
    <div class="brand brand-lg"><span class="brand-mark"></span>Meridan Consulting</div>
    <div class="contact">
      <p>TEL: 4035550187</p>
      <p>mail: info@meridanconsult.com</p>
      <p>WEB: www.meridanconsult.com</p>
      <div class="rule"></div>
      <p>42 - 8 Ave SW | T2P1B4</p>
      <p>calgary canada</p>
    </div>
  </section>

  <section class="sheet folder" aria-label="Präsentationsmappe">
    <div class="brand brand-lg"><span class="brand-mark"></span>Meridan Consulting</div>
  </section>

</body>
</html>
```